New Business Card Design Project

We want a modern business card that catches the attention of other remodeling companies as well as homeowners. We would like it to be informative but still simple.

Target Market(s)

Residential and other Business's

Contact Information for Business Card

TidyKraft
Phone number is 5152947718
Address is
4817 SW 3rd Lane
Des Moines, Iowa 50313
email is tidykraftia@mailorbit.net

Requirements
Must have
• Our tagline
• Honest | Professional | Affordable

```html
<!DOCTYPE html>
<html lang="en">
<head>
<meta charset="utf-8">
<title>TidyKraft Business Card</title>
<link rel="stylesheet" href="https://fonts.googleapis.com/css2?family=Montserrat:wght@800&family=Arimo:wght@400;700&family=Oswald:wght@500&display=swap">
<style>
  :root {
    --page-bg: #3b3b3b;
    --card-white: #ffffff;
    --card-black: #1b1b1b;
    --brand-blue: #0a66c8;
    --brand-orange: #cf500c;
    --ink: #2e2a29;
  }
  * { box-sizing: border-box; margin: 0; padding: 0; }
  html, body {
    width: 1200px; height: 1200px; overflow: hidden;
    background: var(--page-bg);
  }
  .card {
    position: absolute; left: 288px;
    width: 624px; height: 360px;
    overflow: hidden;
  }
  .card--front { top: 178px; background: var(--card-white); }
  .card--back { top: 643px; background: var(--card-black); }

  .wordmark {
    position: absolute; left: 0; right: 0;
    text-align: center;
    font-family: "Montserrat", sans-serif; font-weight: 800;
    color: var(--brand-blue);
    letter-spacing: 0.5px;
    line-height: 1;
  }
  .card--front .wordmark { top: 42px; font-size: 47px; }
  .card--back .wordmark { top: 148px; font-size: 56px; }

  .contact-icon {
    position: absolute; left: 57px;
    width: 34px; height: 34px;
  }
  .contact-text {
    position: absolute; left: 108px;
    font-family: "Arimo", sans-serif; color: var(--ink);
    font-size: 22px; line-height: 26px;
  }
  .contact-text--email { font-size: 19px; }

  .person {
    position: absolute; left: 404px; width: 180px; top: 114px;
    text-align: center; font-family: "Arimo", sans-serif; color: var(--ink);
  }
  .person__name { font-weight: 700; font-size: 29px; line-height: 32px; white-space: nowrap; }
  .person__role { font-size: 22px; line-height: 26px; }

  .tagline-band {
    position: absolute; left: 0; right: 0; top: 300px; height: 37px;
    background: var(--brand-blue);
    display: flex; align-items: center; justify-content: center;
  }
  .tagline {
    font-family: "Oswald", sans-serif; font-weight: 500;
    letter-spacing: 0.2px; white-space: nowrap;
  }
  .tagline-band .tagline { color: var(--card-white); font-size: 23px; }
  .card--back .tagline {
    position: absolute; left: 0; right: 0; top: 212px;
    text-align: center; color: var(--brand-blue); font-size: 21px;
  }
  .tagline__divider { color: inherit; padding: 0 2px; }
  .card--back .tagline__divider { color: var(--brand-orange); }
</style>
</head>
<body>
  <section class="card card--front">
    <div class="wordmark">TIDYKRAFT</div>

    <svg class="contact-icon" style="top:136px" viewBox="0 0 34 34" aria-hidden="true">
      <circle cx="17" cy="17" r="17" fill="var(--brand-orange)"/>
      <path d="M17 7a7 7 0 0 0-7 7c0 5 7 13 7 13s7-8 7-13a7 7 0 0 0-7-7z" fill="#fff"/>
      <circle cx="17" cy="14" r="2.8" fill="var(--brand-orange)"/>
    </svg>
    <div class="contact-text" style="top:140px">4817 SW 3rd Lane<br>Des Moines, Iowa 50313</div>

    <svg class="contact-icon" style="top:198px" viewBox="0 0 34 34" aria-hidden="true">
      <circle cx="17" cy="17" r="17" fill="var(--brand-orange)"/>
      <path d="M11.5 9.5c1-.9 2-.7 2.6.2l1.6 2.4c.5.8.3 1.7-.4 2.2l-1 .8c.8 1.9 2.3 3.5 4.2 4.4l.8-1c.6-.7 1.5-.8 2.3-.3l2.3 1.6c.9.6 1 1.7.1 2.6l-1.2 1.2c-1 1-2.6 1.2-4 .5-4.1-2-7.2-5.2-9-9.3-.6-1.4-.3-2.9.7-3.9z" fill="#fff"/>
    </svg>
    <div class="contact-text" style="top:203px">5152947718</div>

    <svg class="contact-icon" style="top:241px" viewBox="0 0 34 34" aria-hidden="true">
      <circle cx="17" cy="17" r="17" fill="var(--brand-orange)"/>
      <rect x="9" y="11" width="16" height="12" rx="1" fill="#fff"/>
      <path d="M9.5 11.5l7.5 6 7.5-6" fill="none" stroke="var(--brand-orange)" stroke-width="1.6"/>
    </svg>
    <div class="contact-text contact-text--email" style="top:246px">tidykraftia@mailorbit.net</div>

    <div class="person">
      <div class="person__name">DANA KELLER</div>
      <div class="person__role">Owner</div>
    </div>

    <div class="tagline-band">
      <div class="tagline">HONEST <span class="tagline__divider">|</span> PROFESSIONAL <span class="tagline__divider">|</span> AFFORDABLE</div>
    </div>
  </section>

  <section class="card card--back">
    <div class="wordmark">TIDYKRAFT</div>
    <div class="tagline">HONEST <span class="tagline__divider">|</span> PROFESSIONAL <span class="tagline__divider">|</span> AFFORDABLE</div>
  </section>
</body>
</html>
```